Car wrap design for a solar energy installation company - Voltaris

We want a clean looking car wrap design for a solar enerrgy installation company. It must be in our company colours! We want it in bright yellow with black text. Please see attached images for referance and inspiration.

Target Market(s)

Residential consumers

Industry/Entity Type

Renewable energy, solar installations

Font styles to use
Other font styles liked:
• Montserrat semi bold

Colors
FFF300
FFF600
FEFA6F
FFFEC7
FFFEE8

Requirements
Must have
• Copmany name, services & products offered, company colours, easy to read, "bullet points"
Nice to have
• Be creative!
Should not have
• To advanced, to many colours,

```html
<!DOCTYPE html>
<html lang="en">
<head>
<meta charset="utf-8">
<title>Voltaris van wrap</title>
<link rel="stylesheet" href="https://fonts.googleapis.com/css2?family=Montserrat:wght@600;700&display=swap">
<style>
  :root {
    --wrap-yellow: #FFF300;
    --wrap-black: #000000;
    --ink: #231f20;
    --trim: #2b2b2b;
    --glass: #6f7d78;
    --tyre: #1e1e1e;
    --rim: #8c8c8c;
    --lamp-red: #d8202a;
    --lamp-amber: #f39a1e;
    --headlamp: #d9dadb;
    --shadow: #e2e2e2;
    --paper: #ffffff;
  }
  html, body { margin: 0; padding: 0; overflow: hidden; background: var(--paper); }
  .canvas { display: block; width: 1200px; height: 873px; }
  .wrap-text { font-family: "Montserrat", Arial, sans-serif; font-weight: 700; }
  .wrap-text--semi { font-weight: 600; }
  .on-yellow { fill: var(--ink); }
  .on-black { fill: var(--wrap-yellow); }
  .yellow { fill: var(--wrap-yellow); }
  .black { fill: var(--wrap-black); }
  .trim { fill: var(--trim); }
  .glass { fill: var(--glass); }
  .tyre { fill: var(--tyre); }
  .rim { fill: var(--rim); }
  .hub { fill: #555; }
  .lamp-red { fill: var(--lamp-red); }
  .lamp-amber { fill: var(--lamp-amber); }
  .headlamp { fill: var(--headlamp); }
  .ground-shadow { fill: var(--shadow); }
  .seam { stroke: #3a3a3a; stroke-width: 1.5; fill: none; }
  .brand-dot { fill: var(--ink); }
</style>
</head>
<body>
<svg class="canvas" viewBox="0 0 1200 873" xmlns="http://www.w3.org/2000/svg">
  <defs>
    <clipPath id="side-a-dark">
      <path d="M90 98 H315 C345 160 370 240 420 300 L476 347 H90 Z"/>
    </clipPath>
    <clipPath id="side-a-light">
      <path d="M315 98 C345 160 370 240 420 300 L476 347 H770 V90 Z"/>
    </clipPath>
  </defs>

  <!-- ===== Side view, driver side ===== -->
  <g class="van van--side-left">
    <ellipse class="ground-shadow" cx="425" cy="380" rx="390" ry="14"/>
    <path class="yellow" d="M100 98 H500 C560 100 590 120 600 140 L672 218 C720 235 752 255 758 285 V340 H90 V130 Q90 98 100 98 Z"/>
    <path class="black" d="M100 98 H315 C345 160 370 240 420 300 L476 347 H90 V130 Q90 98 100 98 Z"/>
    <path class="seam" d="M94 139 H590"/>
    <path class="seam" d="M316 100 V322 M502 100 V322"/>
    <path class="glass" d="M529 154 H585 L646 214 V222 H529 Z"/>
    <path class="trim" d="M608 187 L651 217 V222 H620 Z"/>
    <path class="headlamp" d="M725 256 Q755 262 758 285 L732 286 Z"/>
    <rect class="lamp-amber" x="674" y="262" width="12" height="5"/>
    <rect class="lamp-red" x="88" y="246" width="16" height="44" rx="2"/>
    <path class="trim" d="M90 308 H200 C205 290 225 278 245 278 C270 278 290 295 294 320 H600 C604 295 630 278 664 278 C700 278 722 300 724 318 H760 V335 Q758 342 740 346 H90 Z"/>
    <g class="wheel"><circle class="tyre" cx="243" cy="341" r="40"/><circle class="rim" cx="243" cy="341" r="28"/><circle class="hub" cx="243" cy="341" r="7"/></g>
    <g class="wheel"><circle class="tyre" cx="664" cy="341" r="40"/><circle class="rim" cx="664" cy="341" r="28"/><circle class="hub" cx="664" cy="341" r="7"/></g>
    <circle class="brand-dot" cx="418" cy="180" r="26"/>
    <text class="wrap-text on-black" x="226" y="174" font-size="20" text-anchor="middle">Renewable energy</text>
    <text class="wrap-text on-black" x="226" y="199" font-size="20" text-anchor="middle">Solar installations</text>
    <g clip-path="url(#side-a-dark)">
      <text class="wrap-text on-black" x="216" y="285" font-size="90" letter-spacing="-1">Voltaris</text>
    </g>
    <g clip-path="url(#side-a-light)">
      <text class="wrap-text on-yellow" x="216" y="285" font-size="90" letter-spacing="-1">Voltaris</text>
    </g>
  </g>

  <!-- ===== Front view ===== -->
  <g class="van van--front">
    <ellipse class="ground-shadow" cx="981" cy="382" rx="120" ry="12"/>
    <path class="yellow" d="M896 100 Q981 92 1068 100 Q1085 150 1092 260 V300 H870 V260 Q877 150 896 100 Z"/>
    <path class="trim" d="M897 100 Q981 92 1067 100 Q1070 110 1068 112 Q981 145 894 112 Q893 108 897 100 Z"/>
    <text class="wrap-text on-black" x="980" y="122" font-size="14" text-anchor="middle">Voltaris</text>
    <path class="trim" d="M883 145 H1077 L1081 218 H879 Z"/>
    <path class="glass" d="M889 150 H1071 L1075 212 H885 Z"/>
    <rect class="trim" x="849" y="186" width="22" height="28" rx="6"/>
    <rect class="trim" x="1091" y="186" width="22" height="28" rx="6"/>
    <circle class="brand-dot" cx="985" cy="234" r="9"/>
    <text class="wrap-text on-yellow" x="981" y="262" font-size="21" text-anchor="middle">Voltaris</text>
    <path class="headlamp" d="M872 255 Q905 256 929 287 H872 Z"/>
    <path class="headlamp" d="M1090 255 Q1057 256 1033 287 H1090 Z"/>
    <rect class="trim" x="934" y="271" width="96" height="22" rx="2"/>
    <rect class="trim" x="870" y="299" width="222" height="46" rx="4"/>
    <rect x="950" y="325" width="62" height="11" fill="#eee"/>
    <rect class="tyre" x="882" y="340" width="26" height="40" rx="4"/>
    <rect class="tyre" x="1054" y="340" width="26" height="40" rx="4"/>
  </g>

  <!-- ===== Side view, passenger side ===== -->
  <g class="van van--side-right">
    <ellipse class="ground-shadow" cx="425" cy="780" rx="390" ry="14"/>
    <path class="yellow" d="M350 494 H752 Q764 496 764 515 V738 H96 V660 Q100 630 130 620 L205 560 L262 530 Q290 500 350 494 Z"/>
    <path class="black" d="M540 522 Q600 494 680 493 H752 Q764 496 764 515 V525 H560 Z"/>
    <path role="img" aria-label="Photo: solar installer in safety gear fitting mounting rails on a tiled roof" fill="#7a5a4c"
      d="M432 741 C432 640 470 560 540 530 Q600 504 680 500 H752 Q764 502 764 520 V738 Z"/>
    <path class="seam" d="M265 535 H760"/>
    <path class="seam" d="M352 496 V722 M538 496 V722"/>
    <path class="glass" d="M233 552 H325 V612 H215 L233 580 Z"/>
    <path class="trim" d="M205 612 L235 588 V615 Z"/>
    <path class="headlamp" d="M96 680 Q100 660 128 653 V680 Z"/>
    <rect class="lamp-amber" x="168" y="657" width="12" height="5"/>
    <rect class="lamp-red" x="750" y="643" width="14" height="44" rx="2"/>
    <circle class="brand-dot" cx="405" cy="519" r="12"/>
    <text class="wrap-text on-yellow" x="405" y="564" font-size="31" text-anchor="middle">Voltaris</text>
    <text class="wrap-text wrap-text--semi on-yellow" x="405" y="580" font-size="12" text-anchor="middle">Solar installations</text>
    <rect class="trim" x="300" y="638" width="26" height="4" rx="2"/>
    <text class="wrap-text on-yellow" x="340" y="682" font-size="31" text-anchor="middle">Voltaris</text>
    <text class="wrap-text on-yellow" x="340" y="703" font-size="23" text-anchor="middle">mobile office</text>
    <path class="trim" d="M96 698 H135 C140 682 160 672 190 672 C220 672 240 688 246 715 H560 C565 690 585 672 608 672 C640 672 658 690 664 712 H764 V730 Q762 740 740 743 H120 Q96 740 96 730 Z"/>
    <g class="wheel"><circle class="tyre" cx="190" cy="735" r="40"/><circle class="rim" cx="190" cy="735" r="28"/><circle class="hub" cx="190" cy="735" r="7"/></g>
    <g class="wheel"><circle class="tyre" cx="608" cy="735" r="40"/><circle class="rim" cx="608" cy="735" r="28"/><circle class="hub" cx="608" cy="735" r="7"/></g>
  </g>

  <!-- ===== Rear view ===== -->
  <g class="van van--rear">
    <ellipse class="ground-shadow" cx="980" cy="782" rx="120" ry="12"/>
    <path class="black" d="M893 497 Q981 489 1068 497 Q1082 540 1087 600 V715 H873 V600 Q878 540 893 497 Z"/>
    <path class="yellow" d="M893 497 Q981 489 1068 497 Q1080 530 1084 580 Q1060 650 981 654 Q900 650 876 580 Q880 530 893 497 Z"/>
    <rect class="yellow" x="873" y="705" width="214" height="11"/>
    <rect class="trim" x="880" y="533" width="16" height="3"/>
    <rect class="trim" x="1064" y="533" width="16" height="3"/>
    <path class="seam" d="M980 500 V712" stroke-opacity="0.4"/>
    <circle class="brand-dot" cx="984" cy="542" r="30"/>
    <text class="wrap-text on-yellow" x="981" y="604" font-size="33" text-anchor="middle">Voltaris</text>
    <text class="wrap-text wrap-text--semi on-yellow" x="981" y="616" font-size="9.5" text-anchor="middle">Renewable energy</text>
    <text class="wrap-text wrap-text--semi on-yellow" x="981" y="628" font-size="9.5" text-anchor="middle">Solar installations</text>
    <rect class="trim" x="945" y="641" width="24" height="4" rx="2"/>
    <rect class="trim" x="992" y="641" width="24" height="4" rx="2"/>
    <text class="wrap-text on-black" x="980" y="676" font-size="16" text-anchor="middle">Your Website</text>
    <text class="wrap-text on-black" x="933" y="698" font-size="12" text-anchor="middle">App Market</text>
    <text class="wrap-text on-black" x="1025" y="698" font-size="12" text-anchor="middle">Play Market</text>
    <rect class="lamp-red" x="869" y="640" width="18" height="48" rx="2"/>
    <rect class="lamp-red" x="1073" y="640" width="18" height="48" rx="2"/>
    <circle class="lamp-amber" cx="878" cy="664" r="5"/>
    <circle class="lamp-amber" cx="1082" cy="664" r="5"/>
    <rect class="trim" x="873" y="716" width="214" height="26" rx="3"/>
    <rect class="tyre" x="879" y="738" width="26" height="40" rx="4"/>
    <rect class="tyre" x="1055" y="738" width="26" height="40" rx="4"/>
  </g>
</svg>
</body>
</html>
```